Dorsey K. Wendell Business Card

We need a business card for our company Dorsey K. Wendell Heating & Plumbing to be distributed to potential customers. It should follow the color scheme of our logo and have a modern upscale and masculine look.

The logo is attached and the info below should also be included:

5187 W. Cedar Brook Rd.
Brookvale, PA 17683

Russell T. Wendell
(717) 592-0817
russelltwendell@fernmail.net
dorseykwendell.net
PA #093148

Industry/Entity Type

Business

Contact Information for Business Card

5187 W. Cedar Brook Rd.
Brookvale, PA 17683

Russell T. Wendell
(717) 592-0817
russelltwendell@fernmail.net
dorseykwendell.net
PA #093148

Colors

Designer to choose colors to be used in the design.

Requirements
Must have
• Information above included

```html
<!DOCTYPE html>
<html lang="en">
<head>
<meta charset="utf-8">
<title>Dorsey K. Wendell Business Card</title>
<link rel="stylesheet" href="https://fonts.googleapis.com/css2?family=Montserrat:wght@400;500;700;800&display=swap">
<style>
  :root {
    --stage: #5f5c64;
    --paper: #ffffff;
    --ink: #1c1c1c;
    --brand-blue: #0d56a6;
    --brand-green: #a6ce39;
    --night: #000000;
  }
  * { margin: 0; padding: 0; box-sizing: border-box; }
  html, body { width: 1200px; height: 675px; overflow: hidden; }
  body {
    background: var(--stage);
    font-family: "Montserrat", Arial, sans-serif;
    position: relative;
  }
  .card {
    position: absolute;
    top: 184px;
    width: 540px;
    height: 308px;
    overflow: hidden;
    box-shadow: 0 10px 24px rgba(0,0,0,.35);
  }
  .card--front { left: 45px; background: var(--paper); }
  .card--back { left: 615px; background: var(--night); }

  .brand {
    position: absolute;
    display: flex;
    align-items: center;
    gap: 12px;
  }
  .brand__mark {
    width: 38px; height: 38px;
    background: var(--brand-blue);
    flex: none;
  }
  .brand__name {
    font-weight: 800;
    font-size: 19px;
    line-height: 1.15;
    color: var(--brand-blue);
    text-transform: uppercase;
    letter-spacing: .5px;
  }
  .card--front .brand { left: 36px; top: 48px; }
  .card--back .brand { left: 120px; top: 125px; }

  .rule {
    position: absolute;
    height: 1.5px;
    background: var(--brand-green);
  }
  .rule--header { left: 36px; right: 36px; top: 112px; }
  .rule--name { left: 40px; width: 220px; top: 196px; }
  .rule--back-top { left: 180px; width: 250px; top: 112px; }
  .rule--back-bottom { left: 120px; width: 230px; top: 190px; }

  .holder {
    position: absolute;
    left: 40px; top: 156px;
    font-size: 25px;
    font-weight: 500;
    color: var(--ink);
  }
  .address {
    position: absolute;
    left: 40px; top: 208px;
    font-size: 12px;
    line-height: 1.5;
    color: var(--ink);
    font-style: normal;
  }
  .contact {
    position: absolute;
    left: 320px; top: 140px;
    list-style: none;
    font-size: 11.5px;
    line-height: 1.65;
    color: var(--ink);
  }
  .contact li { display: flex; align-items: center; gap: 7px; white-space: nowrap; }
  .contact svg { width: 10px; height: 10px; fill: var(--ink); flex: none; }

  .band {
    position: absolute;
    left: 0; bottom: 0;
    width: 410px; height: 16px;
    background: var(--brand-blue);
  }
  .licence {
    position: absolute;
    right: 0; bottom: 0;
    width: 130px; height: 34px;
    background: var(--brand-green);
    color: #fff;
    font-size: 12px;
    font-weight: 500;
    display: flex;
    align-items: center;
    justify-content: center;
  }
</style>
</head>
<body>
  <section class="card card--front" aria-label="Business card front">
    <div class="brand">
      <span class="brand__mark"></span>
      <span class="brand__name">Dorsey K. Wendell<br>Heating &amp; Plumbing</span>
    </div>
    <div class="rule rule--header"></div>
    <h1 class="holder">Russell T. Wendell</h1>
    <div class="rule rule--name"></div>
    <address class="address">5187 W. Cedar Brook Rd.<br>Brookvale, PA 17683</address>
    <ul class="contact">
      <li><svg viewBox="0 0 10 10"><path d="M2 0h2l1 3-1.5 1a6 6 0 0 0 2.5 2.5L7 5l3 1v2a2 2 0 0 1-2 2A8 8 0 0 1 0 2a2 2 0 0 1 2-2z"/></svg>(717) 592-0817</li>
      <li><svg viewBox="0 0 10 10"><path d="M0 2h10v6H0z M0 2l5 3.5L10 2" fill="none" stroke="#1c1c1c" stroke-width="1"/></svg>russelltwendell@fernmail.net</li>
      <li><svg viewBox="0 0 10 10"><circle cx="5" cy="5" r="4.3" fill="none" stroke="#1c1c1c" stroke-width="1"/><path d="M1 5h8M5 1v8" stroke="#1c1c1c" stroke-width=".8"/></svg>dorseykwendell.net</li>
    </ul>
    <div class="band"></div>
    <div class="licence">PA #093148</div>
  </section>

  <section class="card card--back" aria-label="Business card back">
    <div class="rule rule--back-top"></div>
    <div class="brand">
      <span class="brand__mark"></span>
      <span class="brand__name">Dorsey K. Wendell<br>Heating &amp; Plumbing</span>
    </div>
    <div class="rule rule--back-bottom"></div>
  </section>
</body>
</html>
```